BQL Groundworks & Freight Business Card

Can you please design a business card for an Earthworks, Haulage truck and machinery hire company. They also provide sand soil and mulch supply, as well as screening of products. Can you re-create the logo from the attached but add BQL Groundworks & Freight just use the three diamond design.

Target Market(s)

Earthmoving and Transport, Landscapers, Construction

Contact Information for Business Card

ABN 52 907 334 816, Doug Pelham, Managing Director, BQL Groundworks & Freight Mobile 0438 256 904 Email bqlfreight2010@mailvane.net

Font styles to use
Sans Serif

Colors
ec1f27
000000
cbcbcb
ffffff

Requirements
Must have
• Listed on the back, Earthworks | Haulage | Truck and Machinery Hire | Sand, Soil & Mulch Supply | Screening of Products
Nice to have
• Would be good for it to look appealing to a mans man, because it relates to heavy machinery, earthworks, construction etc. Black, red and white would be good maybe with a bit of silver somewhere.
Should not have
• not sure

```html
<!DOCTYPE html>
<html lang="en">
<head>
<meta charset="utf-8">
<title>BQL Groundworks &amp; Freight – Business Card</title>
<link href="https://fonts.googleapis.com/css2?family=PT+Sans+Narrow:wght@400;700&family=Bebas+Neue&display=swap" rel="stylesheet">
<style>
  :root {
    --red: #ec1f27;
    --red-deep: #a8000a;
    --red-mid: #c80812;
    --black: #000000;
    --silver: #cbcbcb;
    --white: #ffffff;
    --bg-light: #fbf7f7;
    --bg-rose: #dcaab0;
  }
  * { margin: 0; padding: 0; box-sizing: border-box; }
  html, body { width: 1200px; height: 1200px; overflow: hidden; }
  body {
    position: relative;
    background: radial-gradient(ellipse at 50% 35%, var(--bg-light) 0%, #efdcdd 55%, var(--bg-rose) 100%);
    font-family: "PT Sans Narrow", "Arial Narrow", sans-serif;
    color: var(--white);
  }

  /* ---------- Front of card ---------- */
  .card-front {
    position: absolute; left: 246px; top: 340px;
    width: 326px; height: 490px;
    background: var(--white);
  }
  .front-band {
    position: absolute; left: 33px; width: 259px; height: 42px;
    background: var(--black);
  }
  .front-band::after {
    content: ""; position: absolute; left: 11px; right: 11px; top: 0; bottom: 0;
    background: var(--red-deep);
  }
  .front-band--top { top: 0; }
  .front-band--bottom { bottom: 0; }
  .front-panel {
    position: absolute; left: 26px; top: 42px; width: 273px; height: 406px;
    border: 4px solid var(--black);
    background: linear-gradient(180deg, var(--red-deep) 0%, var(--red-mid) 35%, var(--red) 100%);
    text-align: center;
  }
  .front-panel > * { position: absolute; left: 0; right: 0; white-space: nowrap; }
  .brand-name {
    top: 78px; display: flex; justify-content: center; align-items: center; gap: 8px;
    font-size: 20px; font-weight: 700;
  }
  .brand-mark { width: 11px; height: 11px; background: var(--white); }
  .service-title { top: 170px; font-size: 24px; }
  .service-line { top: 198px; font-size: 14px; }
  .abn { top: 216px; font-size: 14px; }
  .divider { top: 241px; left: 66px; right: 66px; height: 3px; background: var(--white); }
  .person-name { top: 262px; font-size: 20px; }
  .person-role { top: 289px; font-size: 14px; }
  .contact {
    display: flex; justify-content: center; align-items: center; gap: 8px;
    font-size: 14px;
  }
  .contact--email { top: 325px; }
  .contact--phone { top: 345px; }
  .contact svg { width: 15px; height: 15px; flex: none; }

  /* ---------- Back of card ---------- */
  .card-back {
    position: absolute; left: 630px; top: 337px;
    width: 330px; height: 496px;
    background: linear-gradient(180deg, var(--red-deep) 0%, var(--red) 60%, var(--red-mid) 100%);
  }
  .back-strip {
    position: absolute; left: 0; right: 0; top: 36px; height: 116px;
    border-top: 8px solid var(--black); border-bottom: 8px solid var(--black);
    background: linear-gradient(180deg, #9a9a9a 0%, var(--white) 25%, var(--silver) 55%, var(--white) 80%, #a5a5a5 100%);
    display: flex; justify-content: center; align-items: center; gap: 10px;
  }
  .back-brand {
    font-family: "Bebas Neue", sans-serif;
    font-size: 30px; color: var(--black); letter-spacing: 0.5px; white-space: nowrap;
  }
  .back-mark { width: 14px; height: 14px; background: var(--red-deep); }
  .service-list { list-style: none; }
  .service-item {
    position: absolute; left: 0; right: 0; height: 30px;
    display: flex; justify-content: center; align-items: center; gap: 16px;
    font-family: "Bebas Neue", sans-serif;
    font-size: 29px; line-height: 30px; white-space: nowrap;
  }
  .service-item::before, .service-item::after {
    content: ""; flex: none; width: 8px; height: 8px; background: var(--white); transform: rotate(45deg);
  }
  .back-footer {
    position: absolute; left: 0; right: 0; bottom: 0; height: 20px;
    border-top: 12px solid var(--black); background: var(--white);
  }
</style>
</head>
<body>

<section class="card-front" aria-label="Business card front">
  <div class="front-band front-band--top"></div>
  <div class="front-panel">
    <div class="brand-name"><span class="brand-mark"></span>BQL Groundworks &amp; Freight</div>
    <div class="service-title">Earthworks</div>
    <div class="service-line">Haulage truck and machinery hire company</div>
    <div class="abn">ABN 52 907 334 816</div>
    <div class="divider"></div>
    <div class="person-name">Doug Pelham</div>
    <div class="person-role">Managing Director</div>
    <div class="contact contact--email">
      <svg viewBox="0 0 16 16" aria-hidden="true"><circle cx="8" cy="8" r="7.2" fill="none" stroke="#fff" stroke-width="1.3"/><rect x="4" y="5.2" width="8" height="5.6" fill="none" stroke="#fff" stroke-width="1.1"/><path d="M4 5.4 8 8.6 12 5.4" fill="none" stroke="#fff" stroke-width="1.1"/></svg>
      bqlfreight2010@mailvane.net
    </div>
    <div class="contact contact--phone">
      <svg viewBox="0 0 16 16" aria-hidden="true"><circle cx="8" cy="8" r="7.2" fill="none" stroke="#fff" stroke-width="1.3"/><path d="M5.3 4.4c.4-.3.8-.2 1 .2l.7 1.4c.2.4 0 .7-.3 1l-.4.3c.4 1 1.1 1.8 2.2 2.3l.4-.4c.3-.3.6-.4 1-.2l1.3.7c.4.2.5.7.2 1-.6.8-1.5 1-2.4.6C7 10.6 5.5 9 4.7 7c-.3-1 0-1.9.6-2.6z" fill="#fff"/></svg>
      0438 256 904
    </div>
  </div>
  <div class="front-band front-band--bottom"></div>
</section>

<section class="card-back" aria-label="Business card back">
  <div class="back-strip">
    <span class="back-mark"></span>
    <span class="back-brand">BQL Groundworks &amp; Freight</span>
  </div>
  <ul class="service-list">
    <li class="service-item" style="top:187px">Earthworks</li>
    <li class="service-item" style="top:229px">Haulage</li>
    <li class="service-item" style="top:275px">Truck and Machinery Hire</li>
    <li class="service-item" style="top:321px">Sand, Soil &amp; Mulch Supply</li>
    <li class="service-item" style="top:368px">Screening of Products</li>
  </ul>
  <div class="back-footer"></div>
</section>

</body>
</html>
```